Female Focused - Finance Company needs a website

I need a website for a new company based in London called 'Lorinda Pelham Associates'. The company has been set up with a focus on empowering creativity and encouraging women to engage with finance and build their knowledge and understanding. I am targeting professional women and entrepreneurs in the late 20s to 40s age bracket. The mission is to empower women to achieve financial independence and inspire community and connectivity. I want to create a brand that promotes financial security, growth and connectivity.

The website at this stage can be relatively simple, I just want to be able to have a section about me and the work that I do, have contact details for people to be able to get in touch and find out more.

I run a series of different events and want to have a page whereby I can showcase the events that I am running. They can also use links to click through and register for events. I also want to be able to put images up of previous events that I have run. Maybe having a calendar on the website of different things that are happening.

I am creating a membership club called Hop3Hop and I want to have a page whereby they can find out about the membership and the different options that are available.

I have attached the logo below so you can see the designs so far.

I also own the domain name lorindapelhamassociates.com

```html
<!DOCTYPE html>
<html lang="en">
<head>
<meta charset="utf-8">
<title>Lorinda Pelham Associates</title>
<link href="https://fonts.googleapis.com/css2?family=Baloo+2:wght@400;500;600&family=Montserrat:wght@400;500;600&display=swap" rel="stylesheet">
<style>
:root{
  --purple:#c18ce0;
  --purple-deep:#b27ad9;
  --title:#b680e2;
  --pink:#fde6f3;
  --pink-soft:#fbd9ee;
  --ink:#1d1d1d;
  --muted:#444;
  --white:#fff;
}
*{margin:0;padding:0;box-sizing:border-box}
html,body{width:1200px;height:3950px;overflow:hidden}
body{position:relative;font-family:'Montserrat',sans-serif;color:var(--ink);background:var(--white)}
.abs{position:absolute}
.heading{font-family:'Baloo 2',sans-serif;font-weight:500}
.btn{position:absolute;background:var(--purple);color:var(--white);border-radius:20px;font-size:15px;display:flex;align-items:center;justify-content:center}
.photo{position:absolute}
.section-title{position:absolute;left:0;width:1200px;text-align:center;font-family:'Baloo 2',sans-serif;font-weight:500;font-size:34px;line-height:1}
.arc{position:absolute;left:568px;width:64px;height:30px}
.tri{position:absolute}

/* header */
.header{top:0;left:0;width:1200px;height:88px;background:var(--white)}
.brand{left:147px;top:14px;display:flex;align-items:center;gap:8px}
.brand-dot{width:56px;height:56px;border:1.5px solid var(--ink);border-radius:50%}
.brand-name{font-size:11px;font-weight:500;width:90px;line-height:1.3}
.contact-item{top:34px;font-size:13px;display:flex;align-items:center;gap:8px;white-space:nowrap}
.contact-icon{width:17px;height:17px;border-radius:50%;background:var(--purple);display:flex;align-items:center;justify-content:center;flex:none}
.nav{top:88px;left:0;width:1200px;height:50px;background:var(--purple)}
.nav a{position:absolute;top:15px;color:var(--white);font-size:15.5px;text-decoration:none}
.nav a.active{font-weight:600}
.social{position:absolute;top:16px;width:19px;height:19px;border-radius:50%;background:var(--white)}

/* hero */
.hero{top:138px;left:0;width:1200px;height:479px;background:var(--white);overflow:hidden}
.hero-welcome{left:147px;top:68px;font-size:29px}
.hero-name{left:147px;top:98px;font-size:43px;line-height:1.0;color:var(--title);font-weight:600}
.hero-text{left:147px;top:198px;width:330px;font-size:14.5px;line-height:1.9}

/* about */
.about{top:617px;left:0;width:1200px;height:586px;background:var(--pink)}
.about-text{left:147px;top:158px;width:936px;text-align:center;font-size:15px;line-height:1.85}
.mission{left:368px;top:287px;width:725px;height:153px;background:var(--purple)}
.mission h3{position:absolute;left:130px;top:20px;color:var(--white);font-family:'Baloo 2',sans-serif;font-weight:500;font-size:25px}
.mission p{position:absolute;left:130px;top:56px;width:570px;color:var(--white);font-size:12px;line-height:1.95}

/* events */
.events{top:1203px;left:0;width:1200px;height:935px;background:var(--white)}
.card{position:absolute;background:var(--white);box-shadow:0 1px 6px rgba(0,0,0,.18)}
.card .img{position:absolute;left:0;top:0;width:100%}
.card h4{position:absolute;font-weight:500;font-size:12px}
.card .date{position:absolute;font-size:11.5px}
.card p{position:absolute;font-size:10.5px;line-height:1.85;color:var(--muted)}
.card.lg h4{left:19px;top:420px;font-size:15px}
.card.lg .date{left:19px;top:449px;font-size:14.5px}
.card.lg p{left:22px;top:480px;width:430px;font-size:12.5px;line-height:1.85}
.card.sm h4{left:10px;top:174px}
.card.sm .date{left:10px;top:199px}
.card.sm p{left:12px;top:224px;width:230px}

/* past events */
.past{top:2138px;left:0;width:1200px;height:997px;background:var(--pink);overflow:hidden}

/* membership */
.member{top:3135px;left:0;width:1200px;height:300px;background:var(--white);overflow:hidden}
.member-title{left:359px;top:65px;font-size:33px;color:var(--title);font-weight:500}
.member-text{left:361px;top:122px;width:700px;font-size:14.5px;line-height:1.9}

/* footer */
.footer{top:3435px;left:0;width:1200px;height:515px;background:var(--pink);overflow:hidden}
.footer-mark{left:168px;top:97px;width:160px;height:160px;border:2px solid var(--ink);border-radius:50%;display:flex;align-items:center;justify-content:center;text-align:center;font-size:15px;font-weight:500;line-height:1.4}
.tagline{left:147px;top:300px;font-size:11.5px;letter-spacing:3.5px;color:#777}
.links h5{font-size:15px;font-weight:600;margin-bottom:10px}
.links a{display:block;font-size:15px;color:var(--ink);text-decoration:none;line-height:33px}
.field{position:absolute;background:var(--white);font-size:11.5px;padding:12px 10px;color:#333}
.rule{left:0;top:420px;width:1200px;height:1px;background:#999}
.copy{left:150px;top:464px;font-size:14.5px}
</style>
</head>
<body>

<!-- header -->
<div class="abs header">
  <div class="abs brand"><div class="brand-dot"></div><div class="brand-name">Lorinda Pelham Associates</div></div>
  <div class="abs contact-item" style="left:468px">
    <span class="contact-icon"><svg width="10" height="8" viewBox="0 0 10 8"><rect x=".5" y=".5" width="9" height="7" fill="none" stroke="#fff"/><path d="M.5 .5 5 4.5 9.5 .5" fill="none" stroke="#fff"/></svg></span>
    info@lorindapelhamassociates.com
  </div>
  <div class="abs contact-item" style="left:790px">
    <span class="contact-icon"><svg width="10" height="10" viewBox="0 0 10 10"><path d="M2 1 4 3 3 4.2C3.7 5.5 4.5 6.3 5.8 7L7 6l2 2-1.3 1.4C4.5 9 1 5.5.6 2.3Z" fill="#fff"/></svg></span>
    555-014-2290
  </div>
  <div class="btn" style="left:950px;top:25px;width:124px;height:33px">Login</div>
</div>
<nav class="abs nav">
  <a class="active" style="left:147px">Home</a>
  <a style="left:282px">About Us</a>
  <a style="left:440px">Event</a>
  <a style="left:572px">Gallery</a>
  <a style="left:713px">Contact</a>
  <span class="social" style="left:985px"></span>
  <span class="social" style="left:1015px"></span>
  <span class="social" style="left:1052px"></span>
</nav>

<!-- hero -->
<section class="abs hero">
  <svg class="abs" style="left:0;top:0" width="1200" height="479">
    <circle cx="930" cy="260" r="300" fill="var(--pink)"/>
    <circle cx="560" cy="410" r="190" fill="#e6cff3"/>
  </svg>
  <div class="photo" role="img" aria-label="Group of smiling women stacking their hands together" style="left:500px;top:70px;width:700px;height:409px;background:linear-gradient(90deg,#c9b7c8,#b4c6b0 30%,#d9c1a6 60%,#c9c2bb)"></div>
  <div class="abs hero-welcome">Welcome to</div>
  <div class="abs heading hero-name">Lorinda Pelham<br>Associates</div>
  <p class="abs hero-text">Lorem ipsum dolor sit amet, consectetur adipiscing elit, sed do eiusmod.</p>
  <div class="btn" style="left:147px;top:267px;width:124px;height:33px">Get Started</div>
</section>

<!-- about -->
<section class="abs about">
  <svg class="tri" style="left:0;top:0" width="145" height="102"><polygon points="0,0 142,0 0,100" fill="var(--purple)"/></svg>
  <svg class="arc" style="top:70px" viewBox="0 0 64 30"><path d="M2 28A30 24 0 0 1 62 28" fill="none" stroke="#333" stroke-width="1.3"/></svg>
  <div class="section-title" style="top:102px">About Us</div>
  <p class="abs about-text">Lorem ipsum dolor sit amet, consectetur adipiscing elit, sed do eiusmod tempor incididunt ut labore et dolore magna aliqua. Quis ipsum suspendisse ultrices gravida. Risus commodo viverra maecenas accumsan lacus vel facilisis.</p>
  <div class="abs mission">
    <svg class="abs" style="left:64px;top:46px" width="56" height="56"><circle cx="28" cy="28" r="27" fill="#fff"/><path d="M20 36l6-12 10-6-4 10-12 8zM22 34l-4 4" stroke="var(--purple)" fill="none" stroke-width="1.5"/></svg>
    <h3>Mission</h3>
    <p>The mission is to empower women to achieve financial independence and inspire community and connectivity. I want to create a brand that promotes financial security, growth and connectivity.</p>
  </div>
  <svg class="abs" style="left:136px;top:236px" width="280" height="280"><circle cx="140" cy="140" r="136" fill="#fff" stroke="var(--purple)" stroke-width="5"/></svg>
  <div class="photo" role="img" aria-label="Woman seen from behind at a seminar with an audience" style="left:152px;top:252px;width:248px;height:248px;border-radius:50%;background:linear-gradient(160deg,#e8e2dc,#b49a86 55%,#6e5446)"></div>
  <div class="btn" style="left:216px;top:440px;width:124px;height:33px">Read More</div>
</section>

<!-- events -->
<section class="abs events">
  <svg class="tri" style="left:1056px;top:0" width="144" height="102"><polygon points="0,0 144,0 144,100" fill="var(--purple)"/></svg>
  <svg class="arc" style="top:62px" viewBox="0 0 64 30"><path d="M2 28A30 24 0 0 1 62 28" fill="none" stroke="#333" stroke-width="1.3"/></svg>
  <div class="section-title" style="top:100px">Events</div>

  <div class="card lg" style="left:97px;top:179px;width:475px;height:572px">
    <div class="img" role="img" aria-label="Businesswoman smiling at a desk in a meeting" style="height:391px;background:linear-gradient(135deg,#eef0f3,#b9bec8 50%,#2e3138)"></div>
    <h4>Lorem ipsum dolor sit amet, consectetur adipiscing</h4>
    <div class="date">June 25-2023</div>
    <p>Lorem ipsum dolor sit amet, consectetur adipiscing elit, sed do eiusmod tempor incididunt ut labore et dolore magna aliqua. Ut enim ad minim veniam, quis nostrud exercitation</p>
  </div>
  <div class="card sm" style="left:587px;top:179px;width:256px;height:276px">
    <div class="img" role="img" aria-label="Woman with lanyard standing in an office" style="height:160px;background:linear-gradient(135deg,#b7c6d6,#26324a 60%,#8d9db0)"></div>
    <h4>Lorem ipsum dolor sit amet,</h4><div class="date">June 25-2023</div>
    <p>Lorem ipsum dolor sit amet, consecte-tur adipiscing elit, sed do eiusmod</p>
  </div>
  <div class="card sm" style="left:860px;top:179px;width:256px;height:276px">
    <div class="img" role="img" aria-label="Smiling woman in green shirt holding a laptop" style="height:160px;background:linear-gradient(135deg,#d9e2d5,#2f7a4b 55%,#c8d0c7)"></div>
    <h4>Lorem ipsum dolor sit amet,</h4><div class="date">June 25-2023</div>
    <p>Lorem ipsum dolor sit amet, consecte-tur adipiscing elit, sed do eiusmod</p>
  </div>
  <div class="card sm" style="left:587px;top:469px;width:256px;height:278px">
    <div class="img" role="img" aria-label="Woman using a laptop with glowing digital overlay" style="height:160px;background:linear-gradient(135deg,#1f4f8a,#7fb4e0 50%,#15305a)"></div>
    <h4>Lorem ipsum dolor sit amet,</h4><div class="date">June 25-2023</div>
    <p>Lorem ipsum dolor sit amet, consecte-tur adipiscing elit, sed do eiusmod</p>
  </div>
  <div class="card sm" style="left:860px;top:469px;width:256px;height:278px">
    <div class="img" role="img" aria-label="Hands working on laptop and paperwork" style="height:160px;background:linear-gradient(135deg,#e7ebf0,#9aa9bd 55%,#4b5a72)"></div>
    <h4>Lorem ipsum dolor sit amet,</h4><div class="date">June 25-2023</div>
    <p>Lorem ipsum dolor sit amet, consecte-tur adipiscing elit, sed do eiusmod</p>
  </div>

  <div class="abs" style="left:101px;top:793px;font-size:14px;line-height:1.35"><b style="font-weight:600">Take A Look</b><br>Different Things That Are Happening</div>
  <svg class="abs" style="left:397px;top:799px" width="44" height="20"><path d="M1 10H42M34 3l8 7-8 7" fill="none" stroke="#222" stroke-width="1.6"/></svg>
  <svg class="abs" style="left:474px;top:788px" width="46" height="48"><rect x="1" y="5" width="44" height="42" rx="3" fill="#fff" stroke="#ccc"/><rect x="1" y="5" width="44" height="11" fill="#e8423f"/><rect x="11" y="1" width="3" height="9" fill="#555"/><rect x="32" y="1" width="3" height="9" fill="#555"/><text x="23" y="40" font-size="22" text-anchor="middle" font-family="Montserrat,sans-serif" fill="#222">31</text></svg>
  <div class="btn" style="left:927px;top:797px;width:193px;height:34px">Register For Event</div>
</section>

<!-- past events -->
<section class="abs past">
  <svg class="abs" style="left:0;top:0" width="1200" height="997">
    <circle cx="1226" cy="391" r="170" fill="var(--pink-soft)"/>
    <circle cx="70" cy="770" r="130" fill="var(--pink-soft)"/>
    <polygon points="0,0 142,0 0,100" fill="var(--purple)"/>
  </svg>
  <svg class="arc" style="top:54px" viewBox="0 0 64 30"><path d="M2 28A30 24 0 0 1 62 28" fill="none" stroke="#333" stroke-width="1.3"/></svg>
  <div class="section-title" style="top:88px">Our Past Events</div>
  <div class="photo" role="img" aria-label="Woman smiling at her desk with laptop" style="left:146px;top:170px;width:380px;height:206px;background:linear-gradient(135deg,#f1f2f0,#c9b59c 60%,#8c7560)"></div>
  <div class="photo" role="img" aria-label="Two women talking in a bright office" style="left:540px;top:170px;width:542px;height:206px;background:linear-gradient(90deg,#eeeae6,#a2744f 45%,#3a2d2e 70%,#e3dcd6)"></div>
  <div class="photo" role="img" aria-label="Audience at a seminar with speaker seen from behind" style="left:146px;top:391px;width:542px;height:205px;background:linear-gradient(90deg,#a78670,#e1d9d2 40%,#5b4335 60%,#e5dfd9)"></div>
  <div class="photo" role="img" aria-label="Laughing woman shaking hands" style="left:702px;top:391px;width:380px;height:205px;background:linear-gradient(135deg,#d9c7b6,#7a5a7d 55%,#2c2330)"></div>
  <div class="photo" role="img" aria-label="Woman with lanyard standing in an office" style="left:146px;top:608px;width:303px;height:206px;background:linear-gradient(135deg,#b7c6d6,#26324a 60%,#8d9db0)"></div>
  <div class="photo" role="img" aria-label="Smiling woman in green shirt holding a laptop" style="left:461px;top:608px;width:302px;height:206px;background:linear-gradient(135deg,#d9e2d5,#2f7a4b 55%,#c8d0c7)"></div>
  <div class="photo" role="img" aria-label="Group of women stacking hands together" style="left:777px;top:608px;width:302px;height:206px;background:linear-gradient(90deg,#b4c6b0,#d9c1a6 50%,#c9c2bb)"></div>
  <div class="btn" style="left:538px;top:870px;width:124px;height:34px">View More</div>
</section>

<!-- membership -->
<section class="abs member">
  <svg class="tri" style="left:1065px;top:0" width="135" height="102"><polygon points="0,0 135,0 135,100" fill="var(--purple)"/></svg>
  <div class="photo" role="img" aria-label="Membership card illustration with star badge" style="left:144px;top:68px;width:153px;height:156px;border-radius:10px;background:linear-gradient(180deg,#c79ae6,#8e4fb8)"></div>
  <div class="abs heading member-title">Hop3Hop</div>
  <p class="abs member-text">Lorem ipsum dolor sit amet, consectetur adipiscing elit, sed do eiusmod tempor incididunt ut labore et dolore magna aliqua. Quis ipsum suspendisse ultrices gravida. Risus commodo viverra maecenas accumsan lacus vel facilisis.</p>
  <div class="btn" style="left:359px;top:212px;width:240px;height:33px">Join Our Membership Club</div>
</section>

<!-- footer -->
<footer class="abs footer">
  <svg class="tri" style="left:0;top:0" width="145" height="102"><polygon points="0,0 145,0 0,100" fill="var(--purple)"/></svg>
  <div class="abs footer-mark">Lorinda Pelham<br>Associates</div>
  <div class="abs tagline">EMPOWERING CREATIVITY</div>
  <div class="abs links" style="left:434px;top:113px">
    <h5>Quick Links</h5>
    <a>Home</a><a>About us</a><a>Event</a><a>Gallery</a><a>Contact</a>
  </div>
  <div class="abs heading" style="left:593px;top:103px;font-size:19px">Contact Us</div>
  <div class="field" style="left:593px;top:155px;width:242px;height:39px">Name</div>
  <div class="field" style="left:844px;top:155px;width:238px;height:39px">Telephone</div>
  <div class="field" style="left:593px;top:205px;width:489px;height:38px">Email</div>
  <div class="field" style="left:593px;top:254px;width:489px;height:61px">Message</div>
  <div class="btn" style="left:958px;top:335px;width:124px;height:36px">Submit</div>
  <div class="abs rule"></div>
  <div class="abs copy">© Copyrights 2023 Lorinda Pelham Associates | All Rights Reserved</div>
</footer>

</body>
</html>
```